Ground breaking athletic gear company needs a kick ass business card

We are an American start up athletic gear company that uses a medically proven biohack to boost athletic performance. Heat kills strength and endurance. Our gear helps athletes manage heat better and ultimatley can improve them by up to 10% instantly. Nothing like it out there! Launching this summer.
We are looking for a modern, minimalist design that captures a sporty edge. Check out www.velmarunwear.com, @velmarunwear on instagram for more ideas.

Target Market(s)

25-35 year olds, male and female athletes, vaultlift athletes, competitive runners

Industry/Entity Type

Business

Contact Information for Business Card

Dorian Pellham
Founder
dorianp@velmarunwear.com
www.VelmaRunwear.com
+1 (555) 014-2286

Font styles to use
Sans Serif

Requirements
Must have
• Logo and icon
• All contact information
• dorianp@velmarunwear.com
• +1 (555) 019-4471 M
• +1 (555) 014-2286
Nice to have
• Tag line : "Stay Cool, Run Far"

```html
<!DOCTYPE html>
<html lang="en">
<head>
<meta charset="utf-8">
<title>Velma Runwear — Business Card</title>
<link href="https://fonts.googleapis.com/css2?family=Open+Sans:wght@400;600;700&display=swap" rel="stylesheet">
<style>
  :root {
    --backdrop: #3a3a3a;
    --card: #121212;
    --card-edge: #1c1c1c;
    --ink: #f2f2f2;
    --ink-soft: #cfcfcf;
    --divider: #2a2a2a;
  }
  * { box-sizing: border-box; margin: 0; padding: 0; }
  html, body {
    width: 1200px;
    height: 900px;
    overflow: hidden;
    background: var(--backdrop);
    font-family: "Open Sans", Arial, sans-serif;
    color: var(--ink);
  }
  .stage {
    width: 1200px;
    height: 900px;
    display: flex;
    align-items: center;
    justify-content: center;
    gap: 40px;
  }
  .card {
    position: relative;
    width: 540px;
    height: 309px;
    background: var(--card);
    border-radius: 22px;
    border: 1px solid var(--card-edge);
    box-shadow: 0 14px 30px rgba(0,0,0,.45);
  }
  /* Front */
  .card--front { display: flex; }
  .brand-panel {
    width: 50%;
    display: flex;
    align-items: center;
    justify-content: center;
    border-right: 1px solid var(--divider);
  }
  .wordmark {
    display: flex;
    align-items: center;
    gap: 9px;
    font-weight: 600;
    font-size: 18px;
    letter-spacing: 1.5px;
    text-transform: uppercase;
    white-space: nowrap;
    color: var(--ink);
  }
  .wordmark__mark {
    width: 11px;
    height: 11px;
    border: 1.5px solid var(--ink);
  }
  .contact-panel {
    width: 50%;
    padding: 48px 0 0 30px;
    position: relative;
  }
  .contact-name { font-weight: 700; font-size: 19px; line-height: 1.2; }
  .contact-role { font-size: 13px; color: var(--ink-soft); margin-top: 4px; margin-bottom: 16px; }
  .contact-list { list-style: none; }
  .contact-list li {
    display: flex;
    align-items: center;
    gap: 10px;
    font-size: 13px;
    line-height: 1.6;
    white-space: nowrap;
    color: var(--ink);
  }
  .contact-list svg { width: 11px; height: 11px; flex: none; fill: var(--ink); }
  .tagline {
    position: absolute;
    left: 30px;
    bottom: 48px;
    font-weight: 600;
    font-size: 15px;
    white-space: nowrap;
  }
  /* Back */
  .card--back {
    display: flex;
    align-items: center;
    justify-content: center;
  }
</style>
</head>
<body>
<main class="stage">
  <section class="card card--front">
    <div class="brand-panel">
      <div class="wordmark"><span class="wordmark__mark"></span>Velma Runwear</div>
    </div>
    <div class="contact-panel">
      <h1 class="contact-name">Dorian Pellham</h1>
      <p class="contact-role">Founder</p>
      <ul class="contact-list">
        <li>
          <svg viewBox="0 0 24 24" aria-hidden="true"><path d="M6.6 10.8a15.1 15.1 0 0 0 6.6 6.6l2.2-2.2a1 1 0 0 1 1-.25 11.4 11.4 0 0 0 3.6.57 1 1 0 0 1 1 1V20a1 1 0 0 1-1 1A17 17 0 0 1 3 4a1 1 0 0 1 1-1h3.5a1 1 0 0 1 1 1c0 1.25.2 2.45.57 3.6a1 1 0 0 1-.25 1z"/></svg>
          +1 (555) 014-2286
        </li>
        <li>
          <svg viewBox="0 0 24 24" aria-hidden="true"><path d="M2 5h20v14H2zm2 2v.5l8 5 8-5V7zm0 2.9V17h16V9.9l-8 5z"/></svg>
          dorianp@velmarunwear.com
        </li>
        <li>
          <svg viewBox="0 0 24 24" aria-hidden="true"><path d="M12 2a10 10 0 1 0 0 20 10 10 0 0 0 0-20zm0 2a8 8 0 0 1 0 16 8 8 0 0 1 0-16zm-1 1.5C9 7.5 8 9.6 8 12s1 4.5 3 6.5h2c2-2 3-4.1 3-6.5s-1-4.5-3-6.5zM4.5 11h15v2h-15z"/></svg>
          www.VelmaRunwear.com
        </li>
      </ul>
      <p class="tagline">Stay Cool, Run Far</p>
    </div>
  </section>

  <section class="card card--back">
    <div class="wordmark"><span class="wordmark__mark"></span>Velma Runwear</div>
  </section>
</main>
</body>
</html>
```